Create a landing page for a new product market combination for an international software company

We are a software company being in the BtoB market for over 20 years. Our product is a software tool that allows for very flexible and versatile cost calculations for companies. We sell to all industries in over 40 countries with 500 clients. We have fairly recently seen a succesfull "competitor" (www.quorvel.com) come up in the niche market of IT costing. This competitor has launched an independent platform with regards to managing IT costs (www.PLXguild.org). In this independent platform standards are set, events are organised and books are written. Since our software can handle all type of costing questions we can en already do play a role in IT costing. We have therefore become a sponsor of the PLX guild. Besides that we came accross the opportunity to buy the URL: www.plxsoftware.com Which we did. We are now looking for a design on that landing page that communicates the fact that the visitor has landed with a company that have in depth knowledge on the PLX subject and provide an effective an affordable tooling for PLX. Currently the difference between the professionalism of our own website (www.brandivex.com) and that of the competitor (www.quorvel.com) and the independent council (www.plxguild.org). is too big.

Target Market(s)

BtB with large IT spend

Number of Pages Required

1 page

Colors

Designer to choose colors to be used in the design.

Requirements
Must have
• A proffessional look and feel
Should not have
• Definetely not too much information and wording

```html
<!DOCTYPE html>
<html lang="en">
<head>
<meta charset="utf-8">
<title>PLX Software – Technology Business Management</title>
<link href="https://fonts.googleapis.com/css2?family=Raleway:wght@300;400;500;600;700&display=swap" rel="stylesheet">
<style>
:root{
  --cyan:#16b5e9;
  --cyan-dark:#0ea3d6;
  --ink:#333a3f;
  --ink-soft:#6b7276;
  --band:#cfe0e6;
  --card-dark:#3d3d3d;
  --footer:#141414;
  --footer-bar:#0b0b0b;
  --white:#ffffff;
  --line:#dfe5e8;
}
*{box-sizing:border-box;margin:0;padding:0}
html,body{width:1200px;height:3797px;overflow:hidden}
body{font-family:"Raleway",sans-serif;color:var(--ink);background:var(--white);position:relative}
.abs{position:absolute}
section,header,footer{position:absolute;left:0;width:1200px}
.btn{position:absolute;display:flex;align-items:center;justify-content:center;border-radius:14px;background:var(--cyan);color:var(--white);font-size:11px;font-weight:600}
.btn-dark{background:var(--card-dark)}
.eyebrow{position:absolute;left:0;width:1200px;text-align:center;font-size:8px;letter-spacing:1.5px;text-transform:uppercase;color:var(--ink-soft)}
.eyebrow::before,.eyebrow::after{content:"";display:inline-block;width:18px;height:1px;background:var(--ink-soft);vertical-align:middle;margin:0 6px}
.section-title{position:absolute;left:0;width:1200px;text-align:center;font-size:25px;font-weight:500;color:var(--ink)}
.section-title em{font-style:normal;color:var(--cyan)}
.title-mark{position:absolute;left:590px;width:20px;height:6px;border-bottom:2px solid var(--cyan);border-radius:0 0 10px 10px}
.placeholder{position:absolute}

/* header / hero */
.hero{top:0;height:405px;background:linear-gradient(180deg,#f4f5f6 0%,#e9ebec 100%)}
.topbar{position:absolute;top:0;left:0;width:1200px;height:74px;background:var(--white)}
.nav a{position:absolute;top:45px;font-size:11px;color:var(--ink);text-decoration:none;font-weight:500}
.brand-tab{position:absolute;left:562px;top:0;width:76px;height:80px;background:var(--white);display:flex;align-items:center;justify-content:center;gap:6px;font-size:22px;font-weight:600;color:var(--ink)}
.brand-tab .dot{width:10px;height:10px;background:var(--ink)}
.hero-visual{left:495px;top:74px;width:705px;height:331px;background:linear-gradient(120deg,#f2f3f4 0%,#cfd2d4 45%,#7b8084 75%,#e4e6e7 100%)}
.hero h1{position:absolute;left:248px;top:138px;font-size:24px;font-weight:600;color:var(--ink);line-height:1.2}
.hero h2{position:absolute;left:248px;top:170px;font-size:28px;font-weight:400;color:var(--ink)}
.hero h2 b{font-weight:700}
.hero .tagline{position:absolute;left:248px;top:208px;font-size:16px;color:var(--cyan-dark)}

/* features */
.features{top:405px;height:615px}
.feature{position:absolute;width:200px;text-align:center}
.feature svg{display:block;margin:0 auto 12px}
.feature h3{font-size:12px;font-weight:600;margin-bottom:8px}
.feature p{font-size:9.5px;line-height:1.45;color:var(--ink-soft)}

/* signup */
.signup{top:1020px;height:241px;background:var(--band)}
.field{position:absolute;top:127px;height:25px;border-radius:13px;background:var(--white);font-size:9px;color:#9aa3a7;padding:7px 14px}
.signup .note{position:absolute;top:185px;left:0;width:1200px;text-align:center;font-size:9px;color:var(--ink-soft)}

/* highlight cards */
.highlights{top:1261px;height:250px}
.hl{position:absolute;top:61px;height:134px;padding:20px 24px;text-align:center;color:var(--white)}
.hl h3{font-size:12px;font-weight:600;margin-bottom:8px}
.hl p{font-size:9px;line-height:1.45;text-align:left}
.hl-dark{background:var(--card-dark)}
.hl-light{background:var(--band);color:var(--ink)}

/* functions */
.functions{top:1511px;height:527px;background:var(--band)}
.tab{position:absolute;top:135px;height:25px;border-radius:13px;background:var(--cyan);color:var(--white);font-size:9.5px;font-weight:600;display:flex;align-items:center;justify-content:center}
.tab.active{background:var(--card-dark)}
.panel{position:absolute;left:248px;top:190px;width:702px;height:185px;background:var(--white);border-radius:4px;box-shadow:0 2px 8px rgba(0,0,0,.08)}
.panel::before{content:"";position:absolute;left:182px;top:-10px;border:10px solid transparent;border-top:0;border-bottom-color:var(--white)}
.panel h3{position:absolute;left:289px;top:52px;font-size:14px;font-weight:600}
.panel ul{position:absolute;left:289px;top:78px;list-style:none;font-size:9.5px;line-height:1.5;color:var(--ink-soft)}
.presenter{left:0;top:147px;width:240px;height:380px;background:linear-gradient(180deg,#2f3440 0%,#1e222b 100%);border-radius:90px 90px 0 0}

/* partners */
.partners{top:2038px;height:256px}
.partner-badge{position:absolute;top:163px;height:28px;background:#c9cdd0;border-radius:3px}
.arrow-btn{position:absolute;width:20px;height:20px;border-radius:50%;display:flex;align-items:center;justify-content:center}

/* screenshots */
.screens{top:2294px;height:592px;background:var(--cyan)}
.screens .section-title{color:var(--ink)}
.screens .section-title em{color:var(--white)}
.screens .eyebrow{color:#0d5f7d}
.screens .eyebrow::before,.screens .eyebrow::after{background:#0d5f7d}
.shot-frame{position:absolute;left:294px;top:144px;width:612px;height:304px;background:var(--white);border-radius:8px;padding:8px}
.shot-frame .placeholder{left:8px;top:8px;width:596px;height:288px;background:linear-gradient(180deg,#e3ecf5 0%,#f7f9fb 30%,#eef2f6 100%);border:1px solid #c5d2de}
.shot-side{position:absolute;top:157px;height:272px;background:rgba(255,255,255,.25)}
.dots{position:absolute;top:550px;left:575px;width:50px;height:14px;border-radius:7px;background:rgba(255,255,255,.45);display:flex;gap:5px;align-items:center;justify-content:center}
.dots i{width:5px;height:5px;border-radius:50%;background:var(--white)}

/* news */
.news{top:2886px;height:469px}
.post{position:absolute;top:152px;width:333px;height:228px;background:var(--white);box-shadow:0 2px 10px rgba(0,0,0,.12)}
.post .placeholder{left:0;top:0;width:333px;height:145px}
.post h3{position:absolute;left:18px;top:164px;font-size:14px;font-weight:600;line-height:1.3}
.post .more{position:absolute;right:18px;top:204px;font-size:10px;color:var(--cyan)}

/* footer */
.footer{top:3355px;height:442px;background:var(--footer);color:var(--white)}
.footer .nl-label{position:absolute;left:253px;top:30px;font-size:9px}
.nl-input{position:absolute;left:248px;top:45px;width:200px;height:25px;border-radius:13px 0 0 13px;background:var(--white);font-size:9px;color:#9aa3a7;padding:7px 14px}
.help{position:absolute;left:684px;top:-8px;width:516px;height:76px;background:var(--cyan);clip-path:polygon(18px 0,100% 0,100% 100%,0 100%)}
.help .ask{position:absolute;left:38px;top:15px;font-size:18px;font-weight:600;color:var(--ink)}
.help .phone{position:absolute;left:38px;top:38px;font-size:26px;font-weight:600;color:var(--white)}
.footer-brand{position:absolute;left:248px;top:128px;font-size:48px;font-weight:300;letter-spacing:4px}
.fcol{position:absolute;top:218px;font-size:9.5px;line-height:1.5;color:#d6d9db}
.fcol h4{color:var(--cyan);font-size:10px;font-weight:600;margin-bottom:2px}
.contact-row{position:absolute;left:260px;display:flex;gap:10px;align-items:flex-start;font-size:9.5px;line-height:1.5;color:#d6d9db}
.contact-row .sub{color:var(--cyan)}
.social{position:absolute;left:732px;top:340px;display:flex;gap:8px}
.social i{width:18px;height:18px;border-radius:50%;display:block}
.copyright{position:absolute;left:0;top:413px;width:1200px;height:29px;background:var(--footer-bar);font-size:9px;color:#aeb3b6;padding:9px 248px}
</style>
</head>
<body>

<header class="hero">
  <div class="topbar"></div>
  <div class="placeholder hero-visual" role="img" aria-label="Photo of an open laptop showing a dark dashboard, in soft grey tones"></div>
  <nav class="nav">
    <a style="left:335px">Home</a>
    <a style="left:386px">Product</a>
    <a style="left:444px">Markets</a>
    <a style="left:502px">Company</a>
    <a style="left:657px">Partners</a>
    <a style="left:718px">Events</a>
    <a style="left:774px">Support</a>
    <a style="left:833px">Contact</a>
  </nav>
  <div class="brand-tab"><span class="dot"></span>PLX</div>
  <h1>Technology Business Management</h1>
  <h2>Made <b>Effective</b> And <b>Affordable</b></h2>
  <p class="tagline">Manage Technology as a Business</p>
  <div class="btn" style="left:248px;top:250px;width:110px;height:28px">Request A Demo</div>
</header>

<section class="features">
  <p class="eyebrow" style="top:63px">Features</p>
  <h2 class="section-title" style="top:80px">Best <em>Features</em> Ever</h2>
  <span class="title-mark" style="top:116px"></span>

  <div class="feature" style="left:265px;top:168px">
    <svg width="70" height="70" viewBox="0 0 70 70"><circle cx="35" cy="35" r="30" fill="none" stroke="#e3e8ea" stroke-dasharray="2 3"/><path d="M12 35 Q35 14 58 35 Q35 56 12 35Z" fill="none" stroke="#4b5358" stroke-width="2"/><circle cx="35" cy="35" r="9" fill="var(--cyan)"/></svg>
    <h3>Create Transparency</h3>
    <p>Translate your spending, consumption, and capacity into meaningful perspectives for technology and business decision makers.</p>
  </div>
  <div class="feature" style="left:503px;top:168px">
    <svg width="70" height="70" viewBox="0 0 70 70"><circle cx="35" cy="35" r="30" fill="none" stroke="#e3e8ea" stroke-dasharray="2 3"/><rect x="18" y="40" width="6" height="14" fill="var(--cyan)"/><rect x="28" y="34" width="6" height="20" fill="var(--cyan)"/><rect x="38" y="38" width="6" height="16" fill="var(--cyan)"/><rect x="48" y="28" width="6" height="26" fill="var(--cyan)"/><path d="M18 32 L30 24 L40 29 L54 16" fill="none" stroke="#4b5358" stroke-width="2"/></svg>
    <h3>Shape Business Demand</h3>
    <p>Communicate costs and consumption to business units to drive informed trade-off decisions and better consumption behavior.</p>
  </div>
  <div class="feature" style="left:743px;top:168px">
    <svg width="70" height="70" viewBox="0 0 70 70"><circle cx="35" cy="35" r="30" fill="none" stroke="#e3e8ea" stroke-dasharray="2 3"/><circle cx="35" cy="35" r="16" fill="none" stroke="var(--cyan)" stroke-width="3"/><path d="M40 28 Q35 24 31 27 Q28 31 35 34 Q42 37 38 42 Q34 45 29 41 M35 23 V47" fill="none" stroke="#4b5358" stroke-width="2"/></svg>
    <h3>Deliver Value for Money</h3>
    <p>Maximize value and demonstrate industry-comparable cost-effectiveness for services and innovation you provide.</p>
  </div>
  <div class="feature" style="left:265px;top:395px">
    <svg width="70" height="70" viewBox="0 0 70 70"><circle cx="35" cy="35" r="30" fill="none" stroke="#e3e8ea" stroke-dasharray="2 3"/><circle cx="30" cy="26" r="7" fill="#4b5358"/><path d="M16 52 Q30 32 44 52Z" fill="#4b5358"/><path d="M44 20 L52 28 M52 20 L44 28" stroke="var(--cyan)" stroke-width="2.5"/></svg>
    <h3>Plan &amp; Govern</h3>
    <p>Collaborate to align your annual budget and resource plans to strategic business priorities and manage to the plan.</p>
  </div>
  <div class="feature" style="left:503px;top:395px">
    <svg width="70" height="70" viewBox="0 0 70 70"><circle cx="35" cy="35" r="30" fill="none" stroke="#e3e8ea" stroke-dasharray="2 3"/><path d="M14 44 A21 21 0 0 1 56 44" fill="none" stroke="var(--cyan)" stroke-width="7" stroke-dasharray="8 3"/><path d="M35 44 L46 30" stroke="#4b5358" stroke-width="2.5"/><circle cx="35" cy="44" r="3" fill="#4b5358"/></svg>
    <h3>Cost of Performance</h3>
    <p>Deliver technology, services, and projects efficiently to the business.</p>
  </div>
  <div class="feature" style="left:743px;top:395px">
    <svg width="70" height="70" viewBox="0 0 70 70"><circle cx="35" cy="35" r="30" fill="none" stroke="#e3e8ea" stroke-dasharray="2 3"/><rect x="22" y="22" width="16" height="32" fill="var(--cyan)"/><rect x="38" y="32" width="12" height="22" fill="#4b5358"/><path d="M26 28h3M32 28h3M26 34h3M32 34h3M26 40h3M32 40h3" stroke="#fff" stroke-width="2"/></svg>
    <h3>Business-aligned Portfolio</h3>
    <p>Optimize portfolios to deliver the most value for the level of spending.</p>
  </div>
</section>

<section class="signup">
  <p class="eyebrow" style="top:62px">Opportunity</p>
  <h2 class="section-title" style="top:80px">Signup For <em>Trail</em></h2>
  <span class="title-mark" style="top:114px"></span>
  <div class="field" style="left:395px;width:137px">Your Name</div>
  <div class="field" style="left:549px;width:147px">Email</div>
  <div class="btn" style="left:704px;top:127px;width:101px;height:25px">Submit</div>
  <p class="note">Create Your Account Now!</p>
</section>

<section class="highlights">
  <div class="hl hl-dark" style="left:223px;width:253px;clip-path:polygon(14px 0,100% 0,100% 100%,0 100%)">
    <h3>Get A Grip On Costs</h3>
    <p>Every company wants to improve performance. Success starts with a greater knowledge of how your company works today in terms of costs.</p>
  </div>
  <div class="hl hl-light" style="left:476px;width:258px">
    <h3>Improve Performance</h3>
    <p>Successful companies apply continuous process improvement principles in order to stay ahead of the competition.</p>
  </div>
  <div class="hl hl-dark" style="left:734px;width:246px;clip-path:polygon(0 0,100% 0,calc(100% - 14px) 100%,0 100%)">
    <h3>Outsmart Your Competition</h3>
    <p>Today's winners are those companies that stay innovative and keep their unit costs as low as possible.</p>
  </div>
  <div class="btn" style="left:367px;top:168px;width:84px;height:22px">Read More</div>
  <div class="btn btn-dark" style="left:610px;top:168px;width:84px;height:22px">Read More</div>
  <div class="btn" style="left:866px;top:168px;width:84px;height:22px">Read More</div>
</section>

<section class="functions">
  <p class="eyebrow" style="top:44px">Functions</p>
  <h2 class="section-title" style="top:62px">Product <em>Functions</em></h2>
  <span class="title-mark" style="top:97px"></span>
  <div class="tab" style="left:251px;width:117px">Costing Method</div>
  <div class="tab active" style="left:395px;width:112px">Forecasting Costs</div>
  <div class="tab" style="left:542px;width:114px">Capabilities</div>
  <div class="tab" style="left:686px;width:114px">Budget Information</div>
  <div class="tab" style="left:830px;width:114px">Scenario Analysis</div>
  <div class="placeholder presenter" role="img" aria-label="Illustration of a businessman in a dark suit presenting with an open hand"></div>
  <div class="panel">
    <div class="placeholder" style="left:107px;top:46px;width:139px;height:106px;background:linear-gradient(135deg,#ffffff 0%,#cfd4d7 55%,#5fbf4a 100%)" role="img" aria-label="Illustration of rising bar chart with a green growth arrow"></div>
    <h3>Forecasting Costs And Capacity Needs.</h3>
    <ul>
      <li>Use your pull models to forecast future costs based on expected volumes.</li>
      <li>Estimate cost and capacity needs.</li>
      <li>Rolling forecasts possible.</li>
      <li>User friendly interface.</li>
      <li>Easy to use.</li>
    </ul>
  </div>
  <div class="btn" style="left:542px;top:439px;width:117px;height:25px">View All</div>
</section>

<section class="partners">
  <p class="eyebrow" style="top:66px">Partners</p>
  <h2 class="section-title" style="top:84px">Dedicated <em>Partners</em></h2>
  <span class="title-mark" style="top:119px"></span>
  <div class="arrow-btn" style="left:261px;top:167px;border:1px solid #9aa3a7"><svg width="8" height="8" viewBox="0 0 8 8"><path d="M5 1 L2 4 L5 7" fill="none" stroke="#333" stroke-width="1.5"/></svg></div>
  <div class="partner-badge" style="left:300px;width:126px"></div>
  <div class="partner-badge" style="left:435px;width:24px;border-radius:50%"></div>
  <div class="partner-badge" style="left:495px;width:100px"></div>
  <div class="partner-badge" style="left:640px;width:130px"></div>
  <div class="partner-badge" style="left:805px;width:104px"></div>
  <div class="arrow-btn" style="left:919px;top:167px;background:#333"><svg width="8" height="8" viewBox="0 0 8 8"><path d="M3 1 L6 4 L3 7" fill="none" stroke="#fff" stroke-width="1.5"/></svg></div>
</section>

<section class="screens">
  <p class="eyebrow" style="top:68px">Screenshots</p>
  <h2 class="section-title" style="top:82px">Screenshot <em>In Details</em></h2>
  <span class="title-mark" style="top:117px;border-color:var(--white)"></span>
  <div class="shot-side" style="left:0;width:248px" role="img" aria-label="Faded software screenshot, previous slide"></div>
  <div class="shot-side" style="left:952px;width:248px" role="img" aria-label="Faded software screenshot, next slide"></div>
  <div class="shot-frame">
    <div class="placeholder" role="img" aria-label="Screenshot of the cost modelling software workspace with task panels and a clock widget"></div>
  </div>
  <div class="arrow-btn" style="left:259px;top:319px;width:24px;height:24px;background:var(--white)"><svg width="9" height="9" viewBox="0 0 8 8"><path d="M5 1 L2 4 L5 7" fill="none" stroke="#222" stroke-width="1.6"/></svg></div>
  <div class="arrow-btn" style="left:917px;top:319px;width:24px;height:24px;background:var(--white)"><svg width="9" height="9" viewBox="0 0 8 8"><path d="M3 1 L6 4 L3 7" fill="none" stroke="#222" stroke-width="1.6"/></svg></div>
  <div class="dots"><i></i><i style="opacity:.6"></i><i style="opacity:.6"></i></div>
</section>

<section class="news">
  <p class="eyebrow" style="top:60px">News</p>
  <h2 class="section-title" style="top:78px">News &amp; <em>Blog</em></h2>
  <span class="title-mark" style="top:113px"></span>
  <article class="post" style="left:248px">
    <div class="placeholder" style="background:linear-gradient(180deg,#9a9a9a 0%,#b5b5b5 100%)" role="img" aria-label="PLX guild emblem in orange and white on grey"></div>
    <h3>Brandivex PLX Cost model</h3>
    <span class="more">Read More»</span>
  </article>
  <article class="post" style="left:620px">
    <div class="placeholder" style="background:linear-gradient(180deg,#b8a58c 0%,#6b5a4c 100%)" role="img" aria-label="Group photo of training course participants indoors"></div>
    <h3>Cost Management Training<br>Course Vietnam</h3>
    <span class="more">Read More»</span>
  </article>
</section>

<footer class="footer">
  <p class="nl-label">Sign up to Newsletter for get special offers</p>
  <div class="nl-input">Please Enter Your E-mail</div>
  <div class="btn" style="left:425px;top:45px;width:139px;height:25px">Sign Up</div>
  <div class="help">
    <p class="ask">NEED HELP? CALL US</p>
    <p class="phone">+31 (0)555 010 482</p>
  </div>
  <div class="footer-brand">PLX</div>

  <div class="contact-row" style="top:218px">
    <svg width="14" height="16" viewBox="0 0 14 16"><path d="M7 1 A5 5 0 0 1 12 6 C12 10 7 15 7 15 C7 15 2 10 2 6 A5 5 0 0 1 7 1Z" fill="#fff"/><circle cx="7" cy="6" r="2" fill="var(--footer)"/></svg>
    <div><span class="sub">Ledgerwise USA</span><br>77 Fenwick Lane, Suite 410<br>20814 Marlow Heights, Maryland<br>United States of America</div>
  </div>
  <div class="contact-row" style="top:295px">
    <svg width="14" height="14" viewBox="0 0 14 14"><path d="M3 1 L5 1 L6 4 L4.5 5.5 Q6 8.5 8.5 9.5 L10 8 L13 9 L13 11 Q12 13 10 13 Q2 11 1 3 Q1 1 3 1Z" fill="#fff"/></svg>
    <div>Tel: +1 555 014 2290</div>
  </div>
  <div class="contact-row" style="top:328px">
    <svg width="14" height="12" viewBox="0 0 14 12"><rect x="1" y="1" width="12" height="10" fill="#fff"/><path d="M1 1 L7 6 L13 1" fill="none" stroke="var(--footer)" stroke-width="1.2"/></svg>
    <div>info@brandivex.com<br><span class="sub">View Direction</span></div>
  </div>

  <div class="fcol" style="left:544px">
    <h4>Home</h4>
    Product<br>Markets<br>Company<br>Partners<br>Events<br>Support
  </div>
  <div class="fcol" style="left:732px;width:220px">
    <h4>About Us</h4>
    We are Ledgerwise BV. Every member of our team has extensive experience in cost management using a variety of different products. Together, our combined years of leadership in the field resulted in Brandivex, the tool that incorporates power, functional plasticity and value like no other.
  </div>
  <div class="social">
    <i style="background:#3b5998"></i><i style="background:#d93025"></i><i style="background:#1da1f2"></i><i style="background:#c13584"></i><i style="background:#cb2027"></i>
  </div>
  <div class="copyright">© All Right 2019 Reserved PLX</div>
</footer>

</body>
</html>
```